Redesign of Business Cards to Update them!

We want a full overhaul of our business cards! We have a design that is almost 5 years old and it needs to be updated to be current

Address is 437 Dunmore Lane Suite C San Bernardino CA 92408
PH: 9094718263
Zorlivo.com

Hours M-F 10AM-4PM
Sat and Sunday Closed

```html
<!DOCTYPE html>
<html lang="en">
<head>
<meta charset="utf-8">
<title>Zorlivo Business Cards</title>
<link href="https://fonts.googleapis.com/css2?family=Montserrat:wght@400;500;700;800&display=swap" rel="stylesheet">
<style>
  :root {
    --bg: #2b2b2d;
    --card: #ffffff;
    --red: #f20a0a;
    --red-deep: #c80000;
    --ink: #111111;
    --text: #1c1c1c;
    --muted: #444444;
  }
  * { margin: 0; padding: 0; box-sizing: border-box; }
  html, body { width: 1200px; height: 881px; overflow: hidden; background: var(--bg); }
  .stage { position: relative; width: 1200px; height: 881px; }
  .card {
    position: absolute;
    top: 286px;
    width: 540px;
    height: 309px;
    background: var(--card);
    border-radius: 18px;
    overflow: hidden;
    font-family: "Montserrat", sans-serif;
  }
  .card--front { left: 40px; }
  .card--back { left: 620px; }

  .wordmark {
    display: flex;
    align-items: center;
    gap: 12px;
    font-family: "Montserrat", sans-serif;
    font-weight: 800;
    color: var(--ink);
    letter-spacing: 0.5px;
    line-height: 1.2;
  }
  .wordmark__dot {
    display: block;
    border-radius: 50%;
    background: var(--red);
  }
  .card--front .wordmark {
    position: absolute;
    left: 0; right: 0; top: 0; bottom: 0;
    justify-content: center;
    font-size: 64px;
  }
  .card--front .wordmark__dot { width: 30px; height: 30px; }

  .back-swoosh { position: absolute; left: 0; top: 0; width: 540px; height: 309px; }
  .hours {
    position: absolute;
    right: 36px;
    top: 26px;
    text-align: right;
    color: #ffffff;
    font-weight: 500;
    font-size: 13px;
    line-height: 1.55;
    letter-spacing: 0.6px;
    text-transform: uppercase;
  }
  .card--back .wordmark {
    position: absolute;
    left: 36px;
    top: 156px;
    font-size: 40px;
  }
  .card--back .wordmark__dot { width: 20px; height: 20px; }
  .rule {
    position: absolute;
    left: 36px;
    right: 36px;
    top: 214px;
    height: 1px;
    background: var(--red);
  }
  .contact {
    position: absolute;
    left: 36px;
    right: 36px;
    top: 226px;
    display: flex;
    align-items: baseline;
    gap: 8px;
    font-size: 19px;
    line-height: 1.2;
    color: var(--text);
    font-weight: 400;
    white-space: nowrap;
  }
  .contact__label { color: var(--red); font-weight: 700; }
  .contact__sep { margin: 0 6px; }
  .address {
    position: absolute;
    left: 36px;
    right: 36px;
    top: 258px;
    font-size: 13.5px;
    line-height: 1.3;
    color: var(--muted);
    font-weight: 400;
    white-space: nowrap;
  }
  .address .contact__label { margin-right: 6px; }
</style>
</head>
<body>
<main class="stage">
  <section class="card card--front">
    <div class="wordmark"><span class="wordmark__dot"></span>Zorlivo</div>
  </section>

  <section class="card card--back">
    <svg class="back-swoosh" viewBox="0 0 540 309" aria-hidden="true">
      <defs>
        <linearGradient id="bandGrad" x1="0" y1="0" x2="1" y2="0">
          <stop offset="0" stop-color="#c80000"/>
          <stop offset="1" stop-color="#ff0a0a"/>
        </linearGradient>
      </defs>
      <path d="M0 0 H540 V86 C420 128 250 128 120 128 C70 128 30 132 0 140 Z" fill="url(#bandGrad)"/>
      <path d="M540 86 C420 128 250 128 120 128 C70 128 30 132 0 140 V150 C40 140 90 138 140 138 C290 138 440 128 540 94 Z" fill="#111111"/>
      <path d="M0 150 C40 140 90 138 140 138 C110 141 50 146 0 158 Z" fill="#e00808"/>
    </svg>
    <p class="hours">Hours M-F 10AM-4PM<br>Sat and Sunday Closed</p>
    <div class="wordmark"><span class="wordmark__dot"></span>Zorlivo</div>
    <div class="rule"></div>
    <p class="contact">
      <span class="contact__label">P</span> : <span class="contact__phone">9094718263</span>
      <span class="contact__sep">|</span>
      <span class="contact__label">W</span> : <span class="contact__web">www.zorlivo.com</span>
    </p>
    <p class="address"><span class="contact__label">A</span>437 Dunmore Lane Suite C, San Bernardino CA 92408</p>
  </section>
</main>
</body>
</html>
```